Home page for local retail aggregator

About us: We are a new company that showcases beautiful products available at nearby retail stores. This homepage is meant to display the latest products featured on our site and also allow the user to search, browse with filters, and access their account details.

Currently, our home page looks a little bland. We want the focus of the site to remain on the featured photos and products but the design should be more cohesive. The most successful designs will make more subtle use of our colors, provide intuitive menu controls, and look visually stunning.

This homepage has a few sections:

Header:
-Top Section: will always remain at the top of the page. There should be space for our company name ”zAntelope”, a tagline, and a place for the menus.
-Menus: user must be able to find links for: “My profile” “My Products” “Add Product” “Preview store”
-Bottom section: this will scroll with the user and always remain at the top of the screen providing access to a search box, and filters for “location” “price” and retail categories.

Main Page:
-Each product featured is shown on a tile that includes a photo, title, price, name of store, has space to leave a comment, and include counters for "likes," comments, and "Pods"). “Pods” are bookmark folders. The user’s profile pic is also shown in miniature if they leave a comment.

The final version of the site must be delivered in a fully layered photoshop file and have versions demonstrating what the page will look like both when a user is logged-in and when logged-out.

Target Market(s)

Most of our users are female 18-45. Our customers are retail store owners who want their products to look attractive and professional.

Industry/Entity Type

Retail

Requirements
Must have
• Our logo must be present on the site (attached to project). You're welcome to change the colors in the header but it should look good with our logo.

For reference here are colors we're currently using:
Site text is in Dark Blue: RGB(10/23/47)
Logo color on business cards is light blue: (51/153/204)
Nice to have
• Would love to see new versions of the menus that are more modern and intuitive. Currently we just have links to each individual control. Putting these in a drop-down or re-arranging them would be nice.

```html
<!DOCTYPE html>
<html lang="en">
<head>
<meta charset="utf-8">
<title>zAntelope — Local product search and discovery</title>
<link rel="stylesheet" href="https://fonts.googleapis.com/css2?family=Source+Sans+3:ital,wght@0,400;0,600;0,700;1,400&display=swap">
<style>
  :root{
    --header-blue:#2463b3;
    --header-blue-dark:#1c54a0;
    --ink:#0a172f;
    --brand-blue:#1f5ba8;
    --link-blue:#1d5fae;
    --price-red:#e0263c;
    --page-bg:#e4e5e8;
    --tile-bg:#ffffff;
    --strip-bg:#eeeff1;
    --line:#e2e3e6;
    --muted:#8a8d93;
    --text:#2e3136;
    --footer-bg:#f1f2f4;
  }
  *{box-sizing:border-box;margin:0;padding:0}
  html,body{width:1200px;height:1199px;overflow:hidden}
  body{position:relative;background:var(--page-bg);font-family:"Source Sans 3",Arial,sans-serif;color:var(--ink)}
  ul{list-style:none}

  /* top bar */
  .topbar{position:absolute;left:0;top:0;width:1200px;height:65px;background:linear-gradient(var(--header-blue),var(--header-blue-dark));box-shadow:0 2px 4px rgba(0,0,0,.2)}
  .main-nav a{position:absolute;top:22px;color:#fff;font-size:15px;text-decoration:none}
  .social{position:absolute;top:20px;right:26px;display:flex;gap:14px}
  .social span{width:22px;height:22px;border-radius:50%;background:#fff;opacity:.95}

  /* brand */
  .brand-badge{position:absolute;left:547px;top:2px;width:106px;height:106px;border-radius:50%;background:radial-gradient(#fbfbfc 55%,#e4e6ea);border:3px solid #f5f6f8;box-shadow:0 2px 5px rgba(0,0,0,.25);display:flex;align-items:center;justify-content:center}
  .brand-badge span{width:46px;height:46px;border-radius:50%;background:var(--brand-blue)}
  .brand-name{position:absolute;left:0;width:1200px;top:108px;text-align:center;font-size:25px;font-weight:700;color:var(--brand-blue)}
  .tagline{position:absolute;left:0;width:1200px;top:138px;text-align:center;font-size:15px;color:#5a5d63}

  /* filters */
  .filters{position:absolute;left:20px;top:80px;display:flex;gap:28px}
  .filters a{display:flex;align-items:center;gap:7px;font-size:15px;color:#2b5aa0;text-decoration:none}
  .filters svg{width:18px;height:18px;fill:#5b4a7a}
  .search{position:absolute;left:955px;top:77px;width:227px;height:27px;background:#fff;border:1px solid #d6d8dc;display:flex;align-items:center}
  .search em{flex:1;padding-left:9px;font-size:11px;color:#3d4d6b}
  .search b{width:22px;height:22px;margin-right:2px;background:#eceef1;border:1px solid #d6d8dc;display:flex;align-items:center;justify-content:center}

  /* tiles */
  .tile{position:absolute;width:187px;background:var(--tile-bg);box-shadow:0 1px 3px rgba(0,0,0,.18)}
  .photo{margin:9px 9px 0;height:208px}
  .tile-title{margin:8px 9px 0;font-size:9.5px;font-weight:400;color:var(--link-blue)}
  .tile-meta{display:flex;justify-content:space-between;align-items:center;margin:3px 9px 8px;font-size:9px;color:var(--muted)}
  .price{font-size:11px;color:var(--price-red)}
  .counts{display:flex;gap:12px;padding:5px 8px;background:var(--strip-bg);border-top:1px solid var(--line);font-size:10.5px;color:var(--muted)}
  .counts li{display:flex;align-items:center;gap:3px}
  .counts svg{width:11px;height:11px;fill:none;stroke:#8a8d93;stroke-width:1.3}
  .comments li{display:flex;gap:7px;padding:7px 8px;border-top:1px solid var(--line);background:var(--strip-bg);font-size:9.2px;line-height:1.3;color:var(--text);min-height:43px}
  .comments b{font-weight:700}
  .comments .via{color:var(--muted)}
  .avatar{flex:0 0 25px;width:25px;height:25px}
  .all-comments{padding:8px;border-top:1px solid var(--line);background:var(--strip-bg);text-align:center;font-size:9.5px;font-weight:700;color:var(--text)}
  .reply{display:flex;gap:8px;padding:8px;border-top:1px solid var(--line)}
  .reply .me{background:#e8e9ec}
  .reply-box{flex:1;height:47px;background:#f1f2f3;border:1px solid var(--line);padding:5px 6px;font-size:9.2px;color:var(--muted)}

  .footer{position:absolute;left:0;top:1111px;width:1200px;height:88px;background:var(--footer-bg);border-top:1px solid #d8d9dc;text-align:center;padding-top:31px;font-size:19px;font-weight:600;color:var(--brand-blue)}
</style>
</head>
<body>
<svg width="0" height="0" style="position:absolute">
  <defs>
    <symbol id="i-like" viewBox="0 0 12 12"><path d="M1 5h2v6H1zM3 5l3-4c1 0 1.5.6 1.3 1.6L7 4.5h3c.8 0 1.2.6 1 1.3l-1 4.2c-.2.6-.6 1-1.2 1H3"/></symbol>
    <symbol id="i-comment" viewBox="0 0 12 12"><path d="M1 2h10v6H5l-3 2.5V8H1z"/></symbol>
    <symbol id="i-pod" viewBox="0 0 12 12"><path d="M2 1h8v10H2zM4 3.5h4M4 6h4"/></symbol>
  </defs>
</svg>

<header class="topbar">
  <nav class="main-nav">
    <a href="#" style="left:380px">About</a>
    <a href="#" style="left:478px">Join Us</a>
    <a href="#" style="left:679px">Login</a>
    <a href="#" style="left:771px">Help</a>
  </nav>
  <div class="social" aria-label="Social links"><span></span><span></span><span></span></div>
</header>

<div class="brand-badge"><span></span></div>
<div class="brand-name">zAntelope</div>
<div class="tagline">Local product search and discovery</div>

<nav class="filters">
  <a href="#"><svg viewBox="0 0 20 20"><path d="M10 1a6 6 0 0 0-6 6c0 4.5 6 12 6 12s6-7.5 6-12a6 6 0 0 0-6-6zm0 8.5a2.5 2.5 0 1 1 0-5 2.5 2.5 0 0 1 0 5z"/></svg>Location</a>
  <a href="#"><svg viewBox="0 0 20 20"><path d="M2 3l7-1 9 9-7 7-9-9zm4 2.5a1.5 1.5 0 1 0 0 .01z"/></svg>Price</a>
  <a href="#"><svg viewBox="0 0 20 20"><path d="M2 4h16l-1 4H3zM3 9h14v8H3zM6 11v6M10 11v6M14 11v6"/></svg>Retail Categories</a>
</nav>
<div class="search"><em>What do you want to discover today?</em><b><svg width="10" height="10" viewBox="0 0 10 10"><circle cx="4" cy="4" r="3" fill="none" stroke="#555" stroke-width="1.4"/><path d="M6.3 6.3L9 9" stroke="#555" stroke-width="1.5"/></svg></b></div>

<main class="board">
  <!-- column 1 -->
  <article class="tile" style="left:7px;top:179px">
    <div class="photo" role="img" aria-label="Navy and white colorblock dress" style="background:linear-gradient(#d9d4cb,#f1eee8 38%,#2f4566 68%,#c9c2b6)"></div>
    <h3 class="tile-title">Navy Belmont Colorblock Dress</h3>
    <p class="tile-meta"><span>Minimal</span><span class="price">$50.00</span></p>
    <ul class="counts"><li>10 <svg><use href="#i-like"/></svg></li><li>3 <svg><use href="#i-comment"/></svg></li><li>50 <svg><use href="#i-pod"/></svg></li></ul>
    <ul class="comments">
      <li><span class="avatar" role="img" aria-label="Profile photo" style="background:#7a8a6a"></span><p><b>Mara Whitcombe</b> <span class="via">onto</span> <b>Favorite Things</b></p></li>
      <li><span class="avatar" role="img" aria-label="Profile photo" style="background:#6b5a4e"></span><p><b>Theo Barlow</b> This is awesome!</p></li>
      <li><span class="avatar" role="img" aria-label="Profile photo" style="background:#4a3a33"></span><p><b>Lina Okafor</b> Awesome</p></li>
    </ul>
    <div class="reply"><span class="avatar me" role="img" aria-label="Your profile picture"></span><span class="reply-box">Don't you love this?</span></div>
  </article>
  <article class="tile" style="left:0px;top:606px">
    <div class="photo" role="img" aria-label="Cream ruffled dress with brown sash" style="background:linear-gradient(#cfc8bc,#f2ece0 50%,#c9bfb0)"></div>
    <h3 class="tile-title">Dress like</h3>
    <p class="tile-meta"><span>You and Me Co.</span><span class="price">$60.00</span></p>
    <ul class="counts"><li>10 <svg><use href="#i-like"/></svg></li><li>2 <svg><use href="#i-comment"/></svg></li><li>50 <svg><use href="#i-pod"/></svg></li></ul>
    <ul class="comments">
      <li><span class="avatar" role="img" aria-label="Profile photo" style="background:#a8895f"></span><p><b>Harper Quill</b> <span class="via">onto</span> <b>Quotes</b></p></li>
      <li><span class="avatar" role="img" aria-label="Profile photo" style="background:#a8566a"></span><p><b>Daria Lomax-Reid</b> love, love, love</p></li>
    </ul>
    <div class="reply"><span class="avatar me" role="img" aria-label="Your profile picture"></span><span class="reply-box">Don't you love this?</span></div>
  </article>

  <!-- column 2 -->
  <article class="tile" style="left:206px;top:179px">
    <div class="photo" role="img" aria-label="Tights printed with cat faces and pink shoes" style="height:255px;background:linear-gradient(#c99a88,#e8b8a6 60%,#d04c86 92%)"></div>
    <h3 class="tile-title">Kitten Stockings! Soo cute! I love it</h3>
    <p class="tile-meta"><span>Minimal</span><span class="price">$10.00</span></p>
    <ul class="counts"><li>90 <svg><use href="#i-like"/></svg></li><li>1 <svg><use href="#i-comment"/></svg></li><li>20 <svg><use href="#i-pod"/></svg></li></ul>
    <ul class="comments">
      <li><span class="avatar" role="img" aria-label="Profile photo" style="background:#8a7a6a"></span><p><b>Greta Halloway Finch</b> <span class="via">via</span> <b>June Marlow</b> <span class="via">onto</span> <b>Craft Ideas</b></p></li>
    </ul>
  </article>
  <article class="tile" style="left:198px;top:546px">
    <div class="photo" role="img" aria-label="Faded blue jeans seen from behind" style="background:linear-gradient(#b9bcc0,#4f6f98 30%,#2e4d78 80%,#a8aaae)"></div>
    <h3 class="tile-title">Blue Jeans</h3>
    <p class="tile-meta"><span>Jean and Jeans Co.</span><span class="price">$60.00</span></p>
    <ul class="counts"><li>10 <svg><use href="#i-like"/></svg></li><li>3 <svg><use href="#i-comment"/></svg></li><li>50 <svg><use href="#i-pod"/></svg></li></ul>
    <ul class="comments">
      <li><span class="avatar" role="img" aria-label="Profile photo" style="background:#7a8a6a"></span><p><b>Mara Whitcombe</b> <span class="via">onto</span> <b>Favorite Things</b></p></li>
      <li><span class="avatar" role="img" aria-label="Profile photo" style="background:#6b5a4e"></span><p><b>Theo Barlow</b> This is awesome!</p></li>
      <li><span class="avatar" role="img" aria-label="Profile photo" style="background:#4a3a33"></span><p><b>Lina Okafor</b> Awesome</p></li>
    </ul>
    <div class="reply"><span class="avatar me" role="img" aria-label="Your profile picture"></span><span class="reply-box">Don't you love this?</span></div>
  </article>

  <!-- column 3 -->
  <article class="tile" style="left:405px;top:179px">
    <div class="photo" role="img" aria-label="Four lips in black, pink, orange and blue lipstick" style="height:111px;background:linear-gradient(135deg,#1d1d1f,#ef6fd8 42%,#f47a1c 62%,#3cc6ea)"></div>
    <h3 class="tile-title">Lip for a lip</h3>
    <p class="tile-meta"><span>Kiss</span><span class="price">$30.00</span></p>
    <ul class="counts"><li>90 <svg><use href="#i-like"/></svg></li><li>1 <svg><use href="#i-comment"/></svg></li><li>45 <svg><use href="#i-pod"/></svg></li></ul>
    <ul class="comments">
      <li><span class="avatar" role="img" aria-label="Profile photo" style="background:#6e6456"></span><p><b>Sadie Crane</b> <span class="via">via</span> <b>Nora Vance</b> <span class="via">onto</span> <b>Lovely Tresses</b></p></li>
    </ul>
  </article>
  <article class="tile" style="left:397px;top:413px">
    <div class="photo" role="img" aria-label="Outfit collection: trench coat, white shirt, jeans, handbag and flats" style="height:217px;background:linear-gradient(90deg,#e8cfc0,#fafafa 50%,#2e3f5c 92%)"></div>
    <h3 class="tile-title">My Collection</h3>
    <p class="tile-meta"><span>Collect them all</span><span class="price">$130.00</span></p>
    <ul class="counts"><li>90 <svg><use href="#i-like"/></svg></li><li>6 <svg><use href="#i-comment"/></svg></li><li>45 <svg><use href="#i-pod"/></svg></li></ul>
    <ul class="comments">
      <li><span class="avatar" role="img" aria-label="Profile photo" style="background:#3a5f8a"></span><p><b>Eli n Rosa Pryor</b> Pushed play today for the first time in months. I have to say it felt great!!!!</p></li>
      <li><span class="avatar" role="img" aria-label="Profile photo" style="background:#9a9a9a"></span><p><b>Wendy Lassiter</b> @Ivy Dorsey</p></li>
      <li><span class="avatar" role="img" aria-label="Profile photo" style="background:#c81e2e"></span><p><b>Casey Tolland</b> I have a love-hate relationship with this man!</p></li>
      <li><span class="avatar" role="img" aria-label="Profile photo" style="background:#4a4a5a"></span><p><b>Brynn Caldwell</b> I'm thinking of starting FitLoop 2 soon. I'm so excited!</p></li>
      <li><span class="avatar" role="img" aria-label="Profile photo" style="background:#7a3a3a"></span><p><b>Selena Rae</b> I'm in love with him. SO fun to watch during my workouts.</p></li>
    </ul>
    <div class="all-comments">All 6 comments...</div>
    <div class="reply"><span class="avatar me" role="img" aria-label="Your profile picture"></span><span class="reply-box">This is wonderful?</span></div>
  </article>

  <!-- column 4 -->
  <article class="tile" style="left:606px;top:179px">
    <div class="photo" role="img" aria-label="Outfit collection: trench coat, white shirt, jeans, handbag and flats" style="height:217px;background:linear-gradient(90deg,#e8cfc0,#fafafa 50%,#2e3f5c 92%)"></div>
    <h3 class="tile-title">My Collection</h3>
    <p class="tile-meta"><span>Collect them all</span><span class="price">$130.00</span></p>
    <ul class="counts"><li>90 <svg><use href="#i-like"/></svg></li><li>6 <svg><use href="#i-comment"/></svg></li><li>45 <svg><use href="#i-pod"/></svg></li></ul>
    <ul class="comments">
      <li><span class="avatar" role="img" aria-label="Profile photo" style="background:#3a5f8a"></span><p><b>Eli n Rosa Pryor</b> Pushed play today for the first time in months. I have to say it felt great!!!!</p></li>
      <li><span class="avatar" role="img" aria-label="Profile photo" style="background:#9a9a9a"></span><p><b>Wendy Lassiter</b> @Ivy Dorsey</p></li>
      <li><span class="avatar" role="img" aria-label="Profile photo" style="background:#c81e2e"></span><p><b>Casey Tolland</b> I have a love-hate relationship with this man!</p></li>
      <li><span class="avatar" role="img" aria-label="Profile photo" style="background:#4a4a5a"></span><p><b>Brynn Caldwell</b> I'm thinking of starting FitLoop 2 soon. I'm so excited!</p></li>
      <li><span class="avatar" role="img" aria-label="Profile photo" style="background:#7a3a3a"></span><p><b>Selena Rae</b> I'm in love with him. SO fun to watch during my workouts.</p></li>
    </ul>
    <div class="all-comments">All 6 comments...</div>
  </article>
  <article class="tile" style="left:606px;top:773px">
    <div class="photo" role="img" aria-label="Four lips in black, pink, orange and blue lipstick" style="height:111px;background:linear-gradient(135deg,#1d1d1f,#ef6fd8 42%,#f47a1c 62%,#3cc6ea)"></div>
    <h3 class="tile-title">Lip for a lip</h3>
    <p class="tile-meta"><span>Kiss</span><span class="price">$30.00</span></p>
    <ul class="counts"><li>90 <svg><use href="#i-like"/></svg></li><li>1 <svg><use href="#i-comment"/></svg></li><li>45 <svg><use href="#i-pod"/></svg></li></ul>
    <ul class="comments">
      <li><span class="avatar" role="img" aria-label="Profile photo" style="background:#6e6456"></span><p><b>Sadie Crane</b> <span class="via">via</span> <b>Nora Vance</b> <span class="via">onto</span> <b>Lovely Tresses</b></p></li>
    </ul>
    <div class="reply"><span class="avatar me" role="img" aria-label="Your profile picture"></span><span class="reply-box">Don't you love this?</span></div>
  </article>

  <!-- column 5 -->
  <article class="tile" style="left:806px;top:179px">
    <div class="photo" role="img" aria-label="Faded blue jeans seen from behind" style="background:linear-gradient(#b9bcc0,#4f6f98 30%,#2e4d78 80%,#a8aaae)"></div>
    <h3 class="tile-title">Blue Jeans</h3>
    <p class="tile-meta"><span>Jean and Jeans Co.</span><span class="price">$60.00</span></p>
    <ul class="counts"><li>10 <svg><use href="#i-like"/></svg></li><li>3 <svg><use href="#i-comment"/></svg></li><li>50 <svg><use href="#i-pod"/></svg></li></ul>
    <ul class="comments">
      <li><span class="avatar" role="img" aria-label="Profile photo" style="background:#7a8a6a"></span><p><b>Mara Whitcombe</b> <span class="via">onto</span> <b>Favorite Things</b></p></li>
      <li><span class="avatar" role="img" aria-label="Profile photo" style="background:#6b5a4e"></span><p><b>Theo Barlow</b> This is awesome!</p></li>
      <li><span class="avatar" role="img" aria-label="Profile photo" style="background:#4a3a33"></span><p><b>Lina Okafor</b> Awesome</p></li>
    </ul>
    <div class="reply"><span class="avatar me" role="img" aria-label="Your profile picture"></span><span class="reply-box">Don't you love this?</span></div>
  </article>
  <article class="tile" style="left:806px;top:672px">
    <div class="photo" role="img" aria-label="Tights printed with cat faces and pink shoes" style="height:255px;background:linear-gradient(#c99a88,#e8b8a6 60%,#d04c86 92%)"></div>
    <h3 class="tile-title">Kitten Stockings! Soo cute! I love it</h3>
    <p class="tile-meta"><span>Minimal</span><span class="price">$10.00</span></p>
    <ul class="counts"><li>90 <svg><use href="#i-like"/></svg></li><li>1 <svg><use href="#i-comment"/></svg></li><li>20 <svg><use href="#i-pod"/></svg></li></ul>
    <ul class="comments">
      <li><span class="avatar" role="img" aria-label="Profile photo" style="background:#8a7a6a"></span><p><b>Greta Halloway Finch</b> <span class="via">via</span> <b>June Marlow</b> <span class="via">onto</span> <b>Craft Ideas</b></p></li>
    </ul>
    <div class="reply"><span class="avatar me" role="img" aria-label="Your profile picture"></span><span class="reply-box">This is wonderful?</span></div>
  </article>

  <!-- column 6 -->
  <article class="tile" style="left:1005px;top:179px">
    <div class="photo" role="img" aria-label="Cream ruffled dress with brown sash" style="background:linear-gradient(#cfc8bc,#f2ece0 50%,#c9bfb0)"></div>
    <h3 class="tile-title">Dress like</h3>
    <p class="tile-meta"><span>You and Me Co.</span><span class="price">$60.00</span></p>
    <ul class="counts"><li>10 <svg><use href="#i-like"/></svg></li><li>2 <svg><use href="#i-comment"/></svg></li><li>50 <svg><use href="#i-pod"/></svg></li></ul>
    <ul class="comments">
      <li><span class="avatar" role="img" aria-label="Profile photo" style="background:#a8895f"></span><p><b>Harper Quill</b> <span class="via">onto</span> <b>Quotes</b></p></li>
      <li><span class="avatar" role="img" aria-label="Profile photo" style="background:#a8566a"></span><p><b>Daria Lomax-Reid</b> love, love, love</p></li>
    </ul>
    <div class="reply"><span class="avatar me" role="img" aria-label="Your profile picture"></span><span class="reply-box">Don't you love this?</span></div>
  </article>
  <article class="tile" style="left:1005px;top:632px">
    <div class="photo" role="img" aria-label="Navy and white colorblock dress" style="background:linear-gradient(#d9d4cb,#f1eee8 38%,#2f4566 68%,#c9c2b6)"></div>
    <h3 class="tile-title">Navy Belmont Colorblock Dress</h3>
    <p class="tile-meta"><span>Minimal</span><span class="price">$50.00</span></p>
    <ul class="counts"><li>10 <svg><use href="#i-like"/></svg></li><li>3 <svg><use href="#i-comment"/></svg></li><li>50 <svg><use href="#i-pod"/></svg></li></ul>
    <ul class="comments">
      <li><span class="avatar" role="img" aria-label="Profile photo" style="background:#7a8a6a"></span><p><b>Mara Whitcombe</b> <span class="via">onto</span> <b>Favorite Things</b></p></li>
      <li><span class="avatar" role="img" aria-label="Profile photo" style="background:#6b5a4e"></span><p><b>Theo Barlow</b> This is awesome!</p></li>
      <li><span class="avatar" role="img" aria-label="Profile photo" style="background:#4a3a33"></span><p><b>Lina Okafor</b> Awesome</p></li>
    </ul>
    <div class="reply"><span class="avatar me" role="img" aria-label="Your profile picture"></span><span class="reply-box">Don't you love this?</span></div>
  </article>
</main>

<footer class="footer">Fetching for more&nbsp; exciting discovery...</footer>
</body>
</html>
```